Business Card Design Project - IT Company

Kestrafield Information Technology Solutions
We are an Information Technology Company. We provide computer services to commercial companies. We would like a new card full color front and back with bleeding edge.
We have a logo that you can use or if you want to come up with a new logo that is fine too.
Our colors are mostly Maroon and black but be creative.
Sample Information
Brent R Okafor
4812 W Saguaro Ridge Drive
Suite 410
Phoenix, AZ 85021
O: 602.914.2037
C: 602.468.1290
24/7: 888.914.2037
bokafor@kestrafield.example
www.kestrafield.example
Target Market(s)
Business of all sizes
Industry/Entity Type
Computer
Requirements
Must have
- Bleeding edge
full color on both sides

```html
<!DOCTYPE html>
<html lang="en">
<head>
<meta charset="utf-8">
<title>Kestrafield Business Card</title>
<link rel="stylesheet" href="https://fonts.googleapis.com/css2?family=Raleway:wght@500;600;700&display=swap">
<style>
  :root {
    --page: #ffffff;
    --card: #050505;
    --texture: #1e1e1e;
    --accent: #d01f3c;
    --ink: #ffffff;
  }
  * { margin: 0; padding: 0; box-sizing: border-box; }
  html, body {
    width: 1200px; height: 900px; overflow: hidden;
    background: var(--page);
    font-family: "Raleway", sans-serif;
    color: var(--ink);
  }
  .card {
    position: absolute; left: 132px; top: 124px;
    width: 950px; height: 544px;
    background: var(--card);
    overflow: hidden;
  }
  .card-texture {
    position: absolute; left: 260px; top: 0; width: 690px; height: 470px;
    background: linear-gradient(100deg, var(--card) 0%, var(--texture) 45%, var(--texture) 100%);
  }
  .holder-name {
    position: absolute; left: 24px; top: 186px;
    font-size: 36px; font-weight: 500; letter-spacing: 0.5px;
  }
  .contact-list {
    position: absolute; left: 0; top: 264px;
    display: grid; grid-template-columns: 94px auto; column-gap: 6px; row-gap: 12px;
    font-size: 17px; font-weight: 500;
  }
  .contact-label { color: var(--accent); text-align: right; }
  .brand {
    position: absolute; left: 554px; top: 216px; width: 374px;
  }
  .brand-name {
    font-size: 44px; font-weight: 600; letter-spacing: 2px; line-height: 1;
  }
  .brand-tagline {
    margin-top: 22px;
    font-size: 12.5px; font-weight: 700; letter-spacing: 1.6px; white-space: nowrap;
  }
  .info-band {
    position: absolute; left: 0; top: 470px; width: 950px; height: 50px;
    background: var(--accent);
    display: flex; align-items: center; justify-content: space-between;
    padding: 0 20px 0 18px;
    font-size: 13.5px; font-weight: 600; white-space: nowrap;
  }
  .info-band .band-group { display: flex; gap: 26px; }
</style>
</head>
<body>
  <div class="card">
    <div class="card-texture" role="img" aria-label="Repeating brand letter texture in dark grey"></div>

    <div class="holder-name">BRENT R. OKAFOR</div>

    <div class="contact-list">
      <span class="contact-label">OFFICE:</span><span>602.914.2037</span>
      <span class="contact-label">CELL:</span><span>602.468.1290</span>
      <span class="contact-label">EMAIL:</span><span>BOKAFOR@KESTRAFIELD.EXAMPLE</span>
    </div>

    <div class="brand">
      <div class="brand-name">KESTRAFIELD</div>
      <div class="brand-tagline">INFORMATION TECHNOLOGY SOLUTIONS</div>
    </div>

    <div class="info-band">
      <span>4812 W. SAGUARO RIDGE DRIVE. SUITE 410. PHOENIX, AZ 85021</span>
      <span class="band-group">
        <span>24/7: 888.914.2037</span>
        <span>WEB: WWW.KESTRAFIELD.EXAMPLE</span>
      </span>
    </div>
  </div>
</body>
</html>
```